Flyer-Design für Unterstützung bei Organisation
Zielgruppe
Ich begleite und unterstütze Organisationen und Menschen in Organisationen in ihren Veränderungs- Entwicklungs- und Problemlösungsprozessen ( Führungscoaching, Teamcoaching, Teamentwicklung). Meine Zielgruppe sind Personen in den Berufsrollen Geschäftsführer, HR-Verantwortliche, Führungspersonen, Mitarbeitende in Firmen.
Aufgabenstellung
Ich möchte die Flyer in einem Briefversan mitsenden, wo ich Firmen anschreibe und meine Dienstleistungen vorstelle. Auch möchte ich den Flyer an Orten auflegen, wo mein Zielpublikum Konsultationen in Anspruch nehmen könnte, bsp. Versicherungsagenturen, Hausarztpraxis, Physiotherapie etc.
kurz, interessant und ansprechend die Dienstleistungen gemäss Homepage beschreiben
https://www.lumowegweis.ch/firmen
DIN-Format: DIN A6/5 210 x 105 mm ist optional, lasse mich gerne auch von anderen Vorschlägen überraschen.

```html
<!DOCTYPE html>
<html lang="de">
<head>
<meta charset="utf-8">
<title>Lumowegweis Flyer</title>
<link href="https://fonts.googleapis.com/css2?family=Open+Sans:wght@400;600;700&display=swap" rel="stylesheet">
<style>
  :root {
    --brand-blue: #3a6f9a;
    --sky-top: #8fc0e8;
    --sky-bottom: #a9d0ee;
    --ink: #1d1d1d;
    --paper: #ffffff;
    --backdrop: #eef0f2;
    --field-warm: #b39a6a;
    --field-mist: #e6e2d8;
    --road-grey: #8a8c8e;
  }
  * { box-sizing: border-box; margin: 0; padding: 0; }
  html, body { width: 1200px; height: 1157px; overflow: hidden; }
  body {
    background: var(--backdrop);
    font-family: "Open Sans", Arial, sans-serif;
    color: var(--ink);
    position: relative;
  }
  .flyer {
    position: absolute;
    left: 80px;
    width: 1040px;
    height: 520px;
    background: var(--paper);
    overflow: hidden;
    box-shadow: 0 2px 10px rgba(0,0,0,.12);
  }
  .flyer--front { top: 40px; }
  .flyer--back { top: 597px; }
  .flyer__footer-band {
    position: absolute; left: 0; right: 0; bottom: 0; height: 26px;
    background: var(--brand-blue);
  }
  .brand {
    position: absolute; left: 70px; top: 38px;
    display: flex; align-items: center; gap: 10px;
    font-size: 26px; font-weight: 600; letter-spacing: 1px;
    color: var(--brand-blue); text-transform: uppercase;
  }
  .brand__dot {
    width: 22px; height: 22px; border-radius: 50%; background: var(--brand-blue);
  }
  /* Front side */
  .sky-photo {
    position: absolute; left: 0; right: 0; top: 110px; height: 160px;
    background: linear-gradient(180deg, var(--sky-top), var(--sky-bottom));
  }
  .services {
    position: absolute; left: 0; right: 0; top: 200px;
    display: grid; grid-template-columns: 1fr 1.35fr 1fr;
    padding: 0 40px;
  }
  .service { text-align: center; display: flex; flex-direction: column; align-items: center; padding: 0 10px; }
  .service__badge {
    width: 140px; height: 140px; border-radius: 50%; background: var(--brand-blue);
  }
  .service__title {
    margin-top: 14px; font-size: 22px; font-weight: 700; color: var(--brand-blue);
    letter-spacing: .3px;
  }
  .service__text { margin-top: 2px; font-size: 15px; line-height: 1.33; max-width: 290px; }
  .service--wide .service__text { max-width: 390px; }
  /* Back side */
  .claim {
    position: absolute; left: 345px; top: 48px;
    font-size: 20px; font-weight: 600; line-height: 1.35; color: var(--brand-blue);
  }
  .road-photo {
    position: absolute; left: 0; right: 0; top: 130px; height: 235px;
    background: linear-gradient(180deg, #f3f1ec 0%, var(--field-mist) 35%, var(--field-warm) 65%, var(--road-grey) 100%);
  }
  .pitch {
    position: absolute; left: 70px; top: 384px;
    font-size: 18px; font-weight: 600; line-height: 1.3; color: var(--brand-blue);
  }
  .contact {
    position: absolute; left: 670px; top: 372px;
    font-size: 15px; line-height: 1.4; font-style: normal;
  }
  .contact__title { font-size: 20px; font-weight: 700; color: var(--brand-blue); }
  .contact__row { display: flex; align-items: center; gap: 6px; }
  .contact__row svg { width: 14px; height: 14px; fill: none; stroke: var(--brand-blue); stroke-width: 2; }
  .contact__gap { width: 12px; }
  .contact__web { font-weight: 700; color: var(--brand-blue); }
</style>
</head>
<body>

<section class="flyer flyer--front">
  <div class="brand"><span class="brand__dot"></span>Lumowegweis</div>
  <div class="sky-photo" role="img" aria-label="Foto: vier Vögel im Flug vor blauem Himmel"></div>
  <div class="services">
    <article class="service">
      <div class="service__badge" role="img" aria-label="Symbol: Team aus mehreren Personen"></div>
      <h2 class="service__title">TEAMCOACHING</h2>
      <p class="service__text">Im Team zusammenfinden, motivierte und leistungsfähige Teams haben und/oder Konflikte lösen.</p>
    </article>
    <article class="service service--wide">
      <div class="service__badge" role="img" aria-label="Symbol: Einzelperson"></div>
      <h2 class="service__title">COACHING</h2>
      <p class="service__text">Unterstützung in Führungsaufgaben und Führungskompetenzen, bei Problemen, Konflikten, Veränderungen und Entscheidungen.</p>
    </article>
    <article class="service">
      <div class="service__badge" role="img" aria-label="Symbol: Gehirn"></div>
      <h2 class="service__title">STRESSMANAGEMENT</h2>
      <p class="service__text">Die eigenen Stressfaktoren kennen, angehen und Widerstandsfähiger werden.</p>
    </article>
  </div>
  <div class="flyer__footer-band"></div>
</section>

<section class="flyer flyer--back">
  <div class="brand"><span class="brand__dot"></span>Lumowegweis</div>
  <p class="claim">Ihre Begleitung und Unterstützung in<br>Veränderungs-, Entwicklungs- und Problemlösungsprozessen.</p>
  <div class="road-photo" role="img" aria-label="Foto: gerade Landstrasse durch herbstliche Felder im Morgennebel"></div>
  <p class="pitch">Ob Einzelpersonen oder Team,<br>Sie erhalten eine professionelle Unterstützung und<br>nachhaltige Begleitung. Motivierte und leistungsfähige<br>Mitarbeitende sind ein Gewinn für jede Organisation.</p>
  <address class="contact">
    <div class="contact__title">KONTAKTIEREN SIE MICH!</div>
    <div>Lumowegweis - Selina Aebersold</div>
    <div>Feldgasse 18, 3400 Burgdorf</div>
    <div class="contact__row">
      <svg viewBox="0 0 16 16"><path d="M3 1.5l3 3-1.6 1.8c.9 2 2.3 3.4 4.3 4.3L10.5 9l3 3-1.8 2.2C6.5 13.6 2.4 9.5 1.8 4.3z"/></svg>
      079 482 16 35
      <span class="contact__gap"></span>
      <svg viewBox="0 0 16 16"><path d="M1 7.5L15 1l-4 14-3-6z M8 9l7-8"/></svg>
      info@lumowegweis.ch
    </div>
    <div class="contact__web">www.lumowegweis.ch</div>
  </address>
  <div class="flyer__footer-band"></div>
</section>

</body>
</html>
```